Norvale Telecom Twitter Background

We want to use our existing logo and colours and develop a background for our LinkedIn page and also Twitter page.
Updates

Project Deadline Extended
Reason: Due to very low level of designs submitted I am extending project deadline. Thank you to all who have submitted designs so far.

Industry/Entity Type

Telecom

Requirements
Must have
• Add the company tagline to project
• keeping you connected
• or
• Keeping You Connected
Nice to have
• Fiber optic design element
• In-Building DAS antenna design element
• Ethernet CAT5 design element
• WiFi element

```html
<!DOCTYPE html>
<html lang="en">
<head>
<meta charset="utf-8">
<title>Norvale Telecom – Social Cover Layouts</title>
<link rel="stylesheet" href="https://fonts.googleapis.com/css2?family=Open+Sans:wght@400&family=Exo+2:wght@400;500&display=swap">
<style>
  :root {
    --page: #ffffff;
    --frame-blue: #36a2d0;
    --heading-blue: #2e9ad0;
    --wire-gray: #e0e0e0;
    --wire-dark: #cdcdcd;
    --tile-blue: #0a88c8;
    --ink-white: #ffffff;
    --accent-red: #e8362b;
    --photo-black: #0d0203;
    --photo-red: #8c1a1a;
    --photo-glow: #d23a2a;
    --panel-dark: rgba(12, 4, 5, 0.72);
  }
  * { box-sizing: border-box; margin: 0; padding: 0; }
  html, body { width: 814px; height: 1200px; overflow: hidden; background: var(--page); }
  .canvas { position: relative; width: 814px; height: 1200px; background: var(--page); }
  .abs { position: absolute; }

  /* LinkedIn preview */
  .linkedin-frame { left: 38px; top: 66px; width: 708px; height: 580px; background: var(--frame-blue); }
  .frame-title {
    left: 38px; top: 72px; width: 708px; text-align: center;
    font-family: "Open Sans", sans-serif; font-size: 22px; color: var(--ink-white); letter-spacing: -0.3px;
  }
  .page-mock { left: 80px; top: 106px; width: 619px; height: 540px; background: var(--page); }
  .wire { background: var(--wire-gray); }
  .wire-dark { background: var(--wire-dark); }
  .tile { background: var(--tile-blue); width: 35px; height: 35px; }

  .cover-photo {
    background:
      radial-gradient(ellipse 38% 70% at 52% 20%, rgba(210,58,42,0.75), transparent 70%),
      radial-gradient(ellipse 60% 90% at 30% 60%, rgba(140,26,26,0.55), transparent 75%),
      radial-gradient(ellipse 30% 50% at 92% 30%, rgba(140,26,26,0.5), transparent 75%),
      var(--photo-black);
  }
  .linkedin-cover { left: 118px; top: 266px; width: 553px; height: 173px; overflow: hidden; }
  .brand {
    display: flex; align-items: center; gap: 7px;
    font-family: "Exo 2", sans-serif; font-weight: 500; color: var(--ink-white); white-space: nowrap;
  }
  .brand-dot { width: 9px; height: 9px; border-radius: 50%; background: var(--ink-white); }
  .linkedin-cover .brand { left: 38px; top: 22px; font-size: 19px; }
  .linkedin-tagline {
    left: 0; top: 97px; width: 100%; text-align: center;
    font-family: "Exo 2", sans-serif; font-size: 18px; color: var(--ink-white);
  }
  .linkedin-body {
    left: 0; top: 132px; width: 100%; text-align: center;
    font-family: "Exo 2", sans-serif; font-size: 9.4px; line-height: 12px; color: var(--ink-white);
  }

  .section-label {
    left: 0; top: 680px; width: 814px; text-align: center;
    font-family: "Open Sans", sans-serif; font-size: 22px; color: var(--heading-blue); letter-spacing: -0.3px;
  }

  /* Twitter header */
  .twitter-cover {
    left: 44px; top: 723px; width: 705px; height: 392px; overflow: hidden;
    background:
      radial-gradient(ellipse 30% 45% at 52% 14%, rgba(210,58,42,0.7), transparent 70%),
      radial-gradient(ellipse 45% 40% at 62% 82%, rgba(160,30,30,0.6), transparent 75%),
      radial-gradient(ellipse 40% 55% at 22% 55%, rgba(140,26,26,0.5), transparent 75%),
      var(--photo-black);
  }
  .twitter-panel { left: 553px; top: 77px; width: 152px; height: 204px; background: var(--panel-dark); }
  .twitter-tagline {
    right: 8px; top: 15px; text-align: right; white-space: nowrap;
    font-family: "Exo 2", sans-serif; font-size: 13px; color: var(--accent-red);
  }
  .twitter-body {
    right: 16px; top: 44px; text-align: right; white-space: nowrap;
    font-family: "Exo 2", sans-serif; font-size: 11px; line-height: 12.8px; color: var(--ink-white);
  }
  .twitter-cover .brand { left: 24px; top: 312px; font-size: 23px; }
</style>
</head>
<body>
<main class="canvas">

  <section class="linkedin-mockup">
    <div class="abs linkedin-frame"></div>
    <h2 class="abs frame-title">career cover Photo 974 x 300 - Linkedin</h2>
    <div class="abs page-mock"></div>

    <div class="abs wire" style="left:118px; top:124px; width:543px; height:123px;"></div>
    <div class="abs wire-dark" style="left:137px; top:140px; width:152px; height:92px;"></div>
    <div class="abs wire-dark" style="left:309px; top:140px; width:132px; height:15px;"></div>
    <div class="abs wire-dark" style="left:309px; top:171px; width:333px; height:15px;"></div>

    <div class="abs linkedin-cover">
      <div class="abs cover-photo" style="inset:0;" role="img" aria-label="Close-up photograph of glowing red fibre optic strands on black"></div>
      <div class="abs brand"><span class="brand-dot"></span>Norvale Telecom</div>
      <p class="abs linkedin-tagline">Keeping You Connected</p>
      <p class="abs linkedin-body">Norvale Telecom provides installation and test services for in-building distributed antenna<br>systems (DAS), fiber optic networks, WiFi systems and datacomm / structured cabling.</p>
    </div>

    <div class="abs wire" style="left:118px; top:457px; width:340px; height:189px;"></div>
    <div class="abs wire-dark" style="left:137px; top:496px; width:132px; height:15px;"></div>
    <div class="abs wire-dark" style="left:137px; top:527px; width:300px; height:15px;"></div>
    <div class="abs wire-dark" style="left:137px; top:561px; width:300px; height:85px;"></div>

    <div class="abs wire" style="left:477px; top:457px; width:184px; height:189px;"></div>
    <div class="abs tile" style="left:496px; top:496px;"></div>
    <div class="abs tile" style="left:533px; top:496px;"></div>
    <div class="abs tile" style="left:570px; top:496px;"></div>
    <div class="abs tile" style="left:607px; top:496px;"></div>
    <div class="abs wire-dark" style="left:496px; top:548px; width:146px; height:98px;"></div>
  </section>

  <h2 class="abs section-label">Rev for twitter</h2>

  <section class="abs twitter-cover" role="img" aria-label="Photograph of glowing red fibre optic strands and a red Ethernet cable plug on black">
    <div class="abs twitter-panel">
      <p class="abs twitter-tagline">Keeping You Connected</p>
      <p class="abs twitter-body">Norvale Telecom provides<br>installation and test<br>services for<br>in-building<br>distributed antenna<br>systems (DAS), fiber<br>optic networks, WiFi<br>systems and<br>datacomm /<br>structured cabling.</p>
    </div>
    <div class="abs brand"><span class="brand-dot"></span>Norvale Telecom</div>
  </section>

</main>
</body>
</html>
```